Statement of Professional Excellence

Our school community has create a statement of Professional Excellence at our school (LAM = The Linden Academy at Marbury) This will be shared internally and with candidates interviewing at our school. We'd like a branded graphic that lists in an interesting way our statements:

Professional Excellence at LAM

We honor the whole child while embracing them where they are.
We are mission-driven individuals whose dedication to our students motivates our daily work.
We bring flexible thinking to allow the needs of the students to drive the learning.
We are patient, nurturing, empathetic, and compassionate people.
We value, trust, and support each other.
We learn and we teach.
We lean into and celebrate diversity.
We build trust through genuine partnerships with families.
We are quirky, fun and proud of it.

```html
<!DOCTYPE html>
<html lang="en">
<head>
<meta charset="utf-8">
<title>Professional Excellence at LAM</title>
<link href="https://fonts.googleapis.com/css2?family=Playfair+Display+SC:wght@700&family=Source+Sans+3:ital,wght@1,700&display=swap" rel="stylesheet">
<style>
  :root {
    --navy: #142a4c;
    --navy-deep: #0e2140;
    --gold: #c8a42b;
    --paper: #f3f3f4;
    --white: #ffffff;
    --disc: #ecebea;
  }
  * { box-sizing: border-box; margin: 0; padding: 0; }
  html, body { width: 1180px; height: 1200px; overflow: hidden; }
  body {
    background: var(--paper);
    font-family: "Source Sans 3", "Source Sans Pro", sans-serif;
  }
  .sheet {
    width: 1180px;
    height: 1200px;
    padding: 26px 28px 28px;
    display: flex;
    flex-direction: column;
  }
  .masthead {
    height: 140px;
    flex-shrink: 0;
    display: flex;
    flex-direction: column;
    align-items: center;
    justify-content: center;
    gap: 12px;
  }
  .masthead-rule {
    width: 470px;
    height: 3px;
    background: var(--gold);
  }
  .school-name {
    font-family: "Playfair Display SC", serif;
    font-weight: 700;
    font-size: 38px;
    line-height: 1.05;
    color: var(--navy);
    text-align: center;
    max-width: 560px;
  }
  .title-band {
    margin-top: 14px;
    height: 56px;
    flex-shrink: 0;
    background: var(--gold);
    display: flex;
    align-items: center;
    justify-content: center;
  }
  .title-band h1 {
    font-family: "Playfair Display SC", serif;
    font-weight: 700;
    font-size: 40px;
    letter-spacing: 1.5px;
    color: var(--navy);
    line-height: 1;
  }
  .values-grid {
    margin-top: 22px;
    flex: 1;
    min-height: 0;
    display: grid;
    grid-template-columns: repeat(3, minmax(0, 1fr));
    grid-template-rows: repeat(3, minmax(0, 1fr));
    gap: 24px 24px;
  }
  .value-tile {
    background: linear-gradient(180deg, var(--navy) 0%, var(--navy-deep) 100%);
    display: flex;
    flex-direction: column;
    align-items: center;
    padding: 24px 30px 16px;
    overflow: hidden;
    min-height: 0;
  }
  .value-disc {
    width: 84px;
    height: 84px;
    border-radius: 50%;
    background: var(--disc);
    flex-shrink: 0;
  }
  .value-text {
    margin-top: 30px;
    color: var(--white);
    font-style: italic;
    font-weight: 700;
    font-size: 24px;
    line-height: 1.2;
    text-align: center;
  }
  .value-tile.long .value-text { margin-top: 20px; }
</style>
</head>
<body>
  <main class="sheet">
    <header class="masthead">
      <div class="masthead-rule"></div>
      <div class="school-name">The Linden Academy at Marbury</div>
      <div class="masthead-rule"></div>
    </header>

    <div class="title-band">
      <h1>Characteristics of Professional Excellence</h1>
    </div>

    <section class="values-grid">
      <article class="value-tile">
        <div class="value-disc"></div>
        <p class="value-text">We honor the whole child while embracing them where they are.</p>
      </article>
      <article class="value-tile long">
        <div class="value-disc"></div>
        <p class="value-text">We are mission-driven individuals whose dedication to our students motivates our daily work.</p>
      </article>
      <article class="value-tile">
        <div class="value-disc"></div>
        <p class="value-text">We bring flexible thinking to allow the needs of the students to drive the learning.</p>
      </article>
      <article class="value-tile">
        <div class="value-disc"></div>
        <p class="value-text">We value, trust, and support each other.</p>
      </article>
      <article class="value-tile">
        <div class="value-disc"></div>
        <p class="value-text">We are patient, nurturing, empathetic, and compassionate people.</p>
      </article>
      <article class="value-tile">
        <div class="value-disc"></div>
        <p class="value-text">We learn and we teach.</p>
      </article>
      <article class="value-tile">
        <div class="value-disc"></div>
        <p class="value-text">We lean into and celebrate diversity.</p>
      </article>
      <article class="value-tile">
        <div class="value-disc"></div>
        <p class="value-text">We build trust through genuine partnerships with families.</p>
      </article>
      <article class="value-tile">
        <div class="value-disc"></div>
        <p class="value-text">We are quirky, fun and proud of it.</p>
      </article>
    </section>
  </main>
</body>
</html>
```